Simple Business Cards for Self-employed Coach

Simple business card with a design that includes the QLT logo.
Using either only the logo color or additional colors that match the logo.

Meridian Guides reach deeply into the past, gathering wisdom from East and West, while still staying current with the frontiers of new discovery in cognitive science, genetics, and other disciplines. see https://www.brightharborpath.example/what-is-integral-coaching/

Target Market(s)

Coaching Clients in Tokyo /Asia; in business organizations, but also outside

Industry/Entity Type

Life Coaching

Contact Information for Business Card

Lukas Brenning
Certified Meridian Guide

3-2-48 Kamiyoshi
Nakarino 164-0392
Tokyo, Japan

Phone: +81 70 4817 5062
E-Mail: lukas.brenning@mailora.example

Font styles to use
Sans Serif

Colors
00a990

Requirements
Must have
• include uploaded logo
• color fitting with QLT logo color
Nice to have
• simple, elegant design
Should not have
• clutter

```html
<!DOCTYPE html>
<html lang="en">
<head>
<meta charset="utf-8">
<title>Lukas Brenning – Business Card</title>
<link rel="stylesheet" href="https://fonts.googleapis.com/css2?family=Open+Sans:wght@400;600&display=swap">
<style>
  :root {
    --brand: #1a8073;
    --card: #ffffff;
    --backdrop: #eceeed;
    --shadow: rgba(0, 0, 0, 0.12);
  }
  * { box-sizing: border-box; margin: 0; padding: 0; }
  html, body {
    width: 1200px;
    height: 902px;
    overflow: hidden;
    background: var(--backdrop);
    font-family: "Open Sans", Arial, sans-serif;
    color: var(--brand);
  }
  .card {
    position: absolute;
    left: 100px;
    top: 148px;
    width: 1000px;
    height: 606px;
    background: var(--card);
    box-shadow: 0 8px 30px var(--shadow);
  }
  .brand-mark {
    position: absolute;
    top: 70px;
    right: 80px;
    display: flex;
    align-items: center;
    gap: 14px;
  }
  .brand-mark__square {
    width: 46px;
    height: 46px;
    background: var(--brand);
  }
  .brand-mark__name {
    font-size: 52px;
    font-weight: 600;
    letter-spacing: 10px;
    line-height: 1;
  }
  .identity {
    position: absolute;
    left: 72px;
    top: 292px;
  }
  .identity__name {
    font-size: 54px;
    font-weight: 400;
    letter-spacing: 2px;
    line-height: 1.1;
  }
  .identity__title {
    font-size: 34px;
    font-weight: 400;
    line-height: 1.3;
  }
  .identity__rule {
    width: 440px;
    height: 4px;
    background: var(--brand);
    margin-top: 8px;
  }
  .contact {
    position: absolute;
    left: 72px;
    top: 430px;
    list-style: none;
    font-size: 26px;
    line-height: 1.55;
  }
  .contact__item {
    display: flex;
    align-items: flex-start;
  }
  .contact__icon {
    width: 28px;
    height: 28px;
    margin-top: 6px;
    margin-right: 22px;
    flex: none;
    fill: var(--brand);
  }
</style>
</head>
<body>
  <section class="card">
    <div class="brand-mark">
      <span class="brand-mark__square"></span>
      <span class="brand-mark__name">QLT</span>
    </div>

    <div class="identity">
      <h1 class="identity__name">Lukas Brenning</h1>
      <p class="identity__title">Certified Meridian Guide</p>
      <div class="identity__rule"></div>
    </div>

    <ul class="contact">
      <li class="contact__item">
        <svg class="contact__icon" viewBox="0 0 24 24" aria-hidden="true">
          <path d="M6.6 10.8a15.1 15.1 0 0 0 6.6 6.6l2.2-2.2a1 1 0 0 1 1-.25 11.4 11.4 0 0 0 3.6.57 1 1 0 0 1 1 1V20a1 1 0 0 1-1 1A17 17 0 0 1 3 4a1 1 0 0 1 1-1h3.5a1 1 0 0 1 1 1c0 1.25.2 2.45.57 3.6a1 1 0 0 1-.25 1z"/>
        </svg>
        <span>+81 70 4817 5062</span>
      </li>
      <li class="contact__item">
        <svg class="contact__icon" viewBox="0 0 24 24" aria-hidden="true">
          <path d="M2 5h20v14H2z M4 7v.4l8 5.3 8-5.3V7z" fill-rule="evenodd"/>
        </svg>
        <span>lukas.brenning@mailora.example</span>
      </li>
      <li class="contact__item">
        <svg class="contact__icon" viewBox="0 0 24 24" aria-hidden="true">
          <path d="M12 2 1 12h3v9h6v-6h4v6h6v-9h3z"/>
        </svg>
        <span>3-2-48 Kamiyoshi, Nakarino<br>164-0392, Tokyo, Japan</span>
      </li>
    </ul>
  </section>
</body>
</html>
```